Web Design Project

We need a web design company for a company based in London. We are an online minicab booking service that produces real time quotes on cab journey for consumers. Our colours are currently red and yellow, but do not need to stay that way; it's open to interpretation. Please avoid yellow and black as a colour combination. Our current site is: www.ridelark.co.uk We are looking for a new site to be user-friendly and easy to use, but more polished and professional looking, without using it usability and simplicity. We need to keep the booking capability on each page and it needs to draw in the user's eye. We need a site that is reliable and easy to use, but also fun.

Main objective: keep it simple, like it is now, but polish it up some. Also, we need to be able to add more content to it. And, we will also be adding a login capability for return users.

Target Market(s)

Internet-savvy people aged 18 and older.

Industry/Entity Type

It Company

Requirements
Must have
• Must have the booking widget. However, it doesn't have to be as large as it is now. We are actually thinking to split it over two pages. We will add a few options to the booking widget, such as another via option. The booking widget must be the most noticeable feature on the page. Sans serif font, please.
Should not have
• Should not be too busy and distracting. Please do not use any images of traditional taxis, ie. black cabs from London or yellow cabs from NYC. Our cars do not resemble these and our business cannot be associated with these images.

```html
<!DOCTYPE html>
<html lang="en">
<head>
<meta charset="utf-8">
<title>Ridelark – Book a Cab</title>
<link rel="stylesheet" href="https://fonts.googleapis.com/css2?family=Open+Sans:ital,wght@0,400;0,600;0,700;1,400&family=Signika:wght@400;600&family=Roboto+Condensed:wght@700&display=swap">
<style>
:root{
  --red:#c1202d;
  --red-dark:#9b1620;
  --red-text:#c8202e;
  --blue:#2f5c9c;
  --ink:#333;
  --body:#555;
  --page:#f4f4f4;
  --header-top:#4a4a4a;
  --header-bottom:#262626;
  --footer-top:#2c2c2c;
  --footer-bottom:#4a4a4a;
  --line:#9a9a9a;
  --field:#fff;
  --field-border:#cfcfcf;
  --white:#fff;
}
*{box-sizing:border-box;margin:0;padding:0}
html,body{width:885px;height:1200px;overflow:hidden}
body{position:relative;background:var(--page);font-family:"Open Sans",Arial,sans-serif;color:var(--ink)}
.abs{position:absolute}

/* header */
.site-header{position:absolute;left:0;top:0;width:885px;height:86px;background:linear-gradient(var(--header-top),var(--header-bottom));border-bottom:1px solid #111}
.brand{position:absolute;left:74px;top:22px;display:flex;align-items:center;gap:10px;font-family:"Signika",sans-serif;font-weight:600;font-size:30px;color:var(--white)}
.brand-mark{width:15px;height:15px;background:var(--red)}
.main-nav{position:absolute;left:308px;top:0;height:86px;display:flex}
.main-nav a{display:flex;align-items:center;justify-content:center;height:86px;color:var(--white);text-decoration:none;font-size:13px;border-left:1px solid #1c1c1c;box-shadow:inset 1px 0 0 #555}
.main-nav a.current{background:repeating-linear-gradient(45deg,#3a3a3a 0 3px,#2e2e2e 3px 6px)}
.nav-miles{width:120px}.nav-join{width:80px}.nav-about{width:92px}.nav-contact{width:103px;border-right:1px solid #1c1c1c}
.account{position:absolute;left:722px;top:39px;font-size:10px;color:#ddd}
.account a{color:var(--red-text);text-decoration:underline}

/* how it works */
.how{position:absolute;left:0;top:87px;width:885px;height:338px;background:radial-gradient(ellipse at 50% 35%,#c62330 0%,var(--red) 55%,var(--red-dark) 100%);color:var(--white);border-bottom:3px solid #ddd}
.how h1{position:absolute;top:28px;width:100%;text-align:center;font-family:Arial,sans-serif;font-weight:700;font-size:34px;letter-spacing:.5px}
.step{position:absolute;top:103px;display:flex;gap:26px;align-items:flex-start}
.step-icon{width:60px;height:60px;border-radius:50%;background:#222;flex:none;display:flex;align-items:center;justify-content:center}
.step p{font-size:15px;line-height:19px;margin-top:17px}
.tagline{position:absolute;top:224px;width:100%;text-align:center;font-size:24px}
.subline{position:absolute;top:263px;width:100%;text-align:center;font-size:16px;color:#f0c9cc}

/* booking */
.booking h2{position:absolute;left:53px;top:458px;font-family:"Signika",sans-serif;font-weight:600;font-size:30px;color:var(--red-text)}
.rule{position:absolute;height:1px;background:var(--line)}
.label{position:absolute;left:53px;font-family:Arial,sans-serif;font-size:12px;color:#222}
.label.small{font-size:10.5px}
.field{position:absolute;left:53px;background:var(--field);border:1px solid var(--field-border);font-family:Arial,sans-serif;font-size:10px;color:#888;padding-left:10px;display:flex;align-items:center}
.field.hint{font-style:italic}
.find{position:absolute;left:223px;width:51px;background:#2b2b2b;color:var(--white);font-family:Arial,sans-serif;font-size:12px;font-weight:700;display:flex;align-items:center;justify-content:center}
.select{position:absolute;height:18px;background:var(--field);border:1px solid var(--field-border)}
.select::after{content:"";position:absolute;right:5px;top:5px;border:5px solid transparent;border-top:8px solid #222;border-bottom:0}
.check{position:absolute;width:16px;height:16px;border:1px solid #bbb;background:#fff}
.quote-btn{position:absolute;left:55px;top:1034px;width:216px;height:31px;border-radius:5px;background:linear-gradient(#3c3c3c,#1e1e1e);box-shadow:0 0 0 2px #ddd;color:var(--white);font-family:"Signika",sans-serif;font-size:15px;display:flex;align-items:center;justify-content:center}
.divider{position:absolute;left:335px;top:498px;width:1px;height:567px;background:var(--line)}

/* why */
.why h2{position:absolute;left:376px;top:462px;font-family:"Roboto Condensed",Arial,sans-serif;font-weight:700;font-size:24px;color:var(--blue)}
.why h3{position:absolute;left:376px;font-family:Arial,sans-serif;font-size:13px;font-weight:700;color:#222}
.why p{position:absolute;left:376px;width:460px;font-family:Arial,sans-serif;font-size:11.5px;line-height:21px;color:var(--body)}
.stories h2{position:absolute;left:376px;top:750px;font-family:Arial,sans-serif;font-size:18px;font-weight:700;color:#222}
.story{position:absolute;left:376px;top:799px;width:462px;font-family:Arial,sans-serif;font-size:11.5px;line-height:20px;color:var(--body)}
.share{position:absolute;left:376px;top:982px;font-family:Arial,sans-serif;font-size:13px;font-style:italic;color:#222}
.share a{color:var(--red-text);font-size:16px;text-decoration:underline}

/* footer */
.site-footer{position:absolute;left:0;top:1103px;width:885px;height:97px;background:linear-gradient(var(--footer-top),var(--footer-bottom));border-top:2px solid #ccc}
.copyright{position:absolute;top:32px;width:100%;text-align:center;font-family:Arial,sans-serif;font-size:10px;color:var(--white);line-height:15px}
.copyright .name{color:var(--red-text)}
.copyright u{color:var(--white)}
.social{position:absolute;top:34px;width:26px;height:26px;border-radius:50%;background:#bdbdbd}
</style>
</head>
<body>

<header class="site-header">
  <div class="brand"><span class="brand-mark"></span>Ridelark</div>
  <nav class="main-nav">
    <a class="nav-miles current" href="#">Ridelark Miles</a>
    <a class="nav-join" href="#">Join Us</a>
    <a class="nav-about" href="#">About Us</a>
    <a class="nav-contact" href="#">Contact Us</a>
  </nav>
  <div class="account"><a href="#">Login</a> &nbsp;or&nbsp; <a href="#">Sign up</a></div>
</header>

<section class="how">
  <h1>HOW IT WORKS?</h1>
  <div class="step" style="left:36px">
    <div class="step-icon">
      <svg width="26" height="30" viewBox="0 0 26 30"><rect x="2" y="1" width="22" height="28" fill="#fff"/><g stroke="#222" stroke-width="2"><line x1="6" y1="7" x2="20" y2="7"/><line x1="6" y1="12" x2="20" y2="12"/><line x1="6" y1="17" x2="20" y2="17"/><line x1="6" y1="22" x2="20" y2="22"/></g></svg>
    </div>
    <p>Enter your route</p>
  </div>
  <div class="step" style="left:290px">
    <div class="step-icon">
      <svg width="36" height="32" viewBox="0 0 36 32" fill="none" stroke="#fff" stroke-width="2"><line x1="18" y1="3" x2="18" y2="28"/><line x1="4" y1="7" x2="32" y2="5"/><line x1="11" y1="29" x2="25" y2="29"/><path d="M4 7 L0 18 H8 Z"/><path d="M32 5 L28 16 H36 Z"/></svg>
    </div>
    <p>Quickly compare<br>taxi fares</p>
  </div>
  <div class="step" style="left:579px">
    <div class="step-icon">
      <svg width="32" height="24" viewBox="0 0 32 24"><rect x="1" y="2" width="30" height="20" fill="#fff"/><path d="M1 2 L16 14 L31 2" fill="none" stroke="#222" stroke-width="2"/></svg>
    </div>
    <p>Get your travel con-<br>firmed on your phone by<br>SMS.</p>
  </div>
  <p class="tagline">As easy as opening the cab's door</p>
  <p class="subline">Its free, dependable and with no obligation</p>
</section>

<section class="booking">
  <h2>Book a Cab</h2>
  <div class="rule" style="left:53px;top:500px;width:230px"></div>

  <div class="label" style="top:511px">Pick me up from:</div>
  <div class="field hint" style="top:529px;width:170px;height:26px">e.g. &nbsp;pick up address or post code</div>
  <div class="find" style="top:529px;height:26px">Find</div>

  <div class="label" style="top:567px">Drop me at:</div>
  <div class="field hint" style="top:587px;width:170px;height:26px">e.g. &nbsp;drop address or post code</div>
  <div class="find" style="top:587px;height:26px">Find</div>

  <div class="label" style="top:622px">Pick up date and time:</div>
  <div class="field" style="top:643px;width:170px;height:25px">5 Apr 2012 @ 12:02</div>
  <svg class="abs" style="left:240px;top:637px" width="34" height="30" viewBox="0 0 34 30"><rect x="1" y="4" width="32" height="25" fill="#fff" stroke="#bbb"/><rect x="1" y="4" width="32" height="7" fill="#3a6aa8"/><g fill="#ccc"><rect x="5" y="14" width="4" height="3"/><rect x="12" y="14" width="4" height="3"/><rect x="19" y="14" width="4" height="3"/><rect x="26" y="14" width="4" height="3"/><rect x="5" y="20" width="4" height="3"/><rect x="12" y="20" width="4" height="3"/><rect x="19" y="20" width="4" height="3"/><rect x="26" y="20" width="4" height="3"/></g><g fill="#555"><rect x="8" y="1" width="2" height="6"/><rect x="24" y="1" width="2" height="6"/></g></svg>

  <div class="label small" style="top:684px">Just pick me up in</div>
  <div class="select" style="left:147px;top:681px;width:75px"></div>

  <div class="label small" style="top:710px">Passenger:</div>
  <div class="select" style="left:130px;top:707px;width:43px"></div>
  <div class="label small" style="left:173px;top:710px">Luggage:</div>
  <div class="select" style="left:223px;top:707px;width:43px"></div>

  <div class="check" style="left:53px;top:740px"></div>
  <svg class="abs" style="left:54px;top:736px" width="18" height="18" viewBox="0 0 18 18"><path d="M3 9 L7 14 L16 2" fill="none" stroke="#333" stroke-width="2"/></svg>
  <div class="label" style="left:78px;top:741px">Return Journey</div>
  <div class="check" style="left:175px;top:740px"></div>
  <div class="label" style="left:200px;top:741px">Extras</div>

  <div class="label" style="top:767px">Mobile Number:</div>
  <div class="field" style="top:787px;width:221px;height:25px"></div>
  <div class="label" style="top:823px">Name:</div>
  <div class="field" style="top:841px;width:221px;height:25px"></div>
  <div class="label" style="top:878px">Email:</div>
  <div class="field" style="top:897px;width:221px;height:25px"></div>
  <div class="label" style="top:934px">Comments:</div>
  <div class="field" style="top:952px;width:221px;height:58px"></div>

  <div class="quote-btn">Get your no obligation quotes</div>
</section>

<div class="divider"></div>

<section class="why">
  <h2>Why Ridelark?</h2>
  <div class="rule" style="left:376px;top:500px;width:458px"></div>
  <h3 style="top:523px">Price</h3>
  <p style="top:546px">Ridelark guarantees that you get the best deal for your travel, as you get quotes from several cab companies.</p>
  <h3 style="top:596px">No fees</h3>
  <p style="top:619px">There's absolutely no cost for you to use our service.</p>
  <h3 style="top:649px">Coverage</h3>
  <p style="top:672px">Ridelark has the largest database of licensed minicab operators. You can use Ridelark wherever you are in greater London.</p>
</section>

<section class="stories">
  <h2>The best stories from our community</h2>
  <div class="rule" style="left:376px;top:780px;width:458px"></div>
  <p class="story">I recently hit London for a girlie night on the town with my bestie. After a little too much champagne, we had a stupid argument and decided to leave the club early. In the cab on our way home, we didn't say one word to each other. The driver who could sense we were both upset however, had other plans. He randomly started singing Velvet Tones' Night Waltz! My best friend and I were in shock, we looked at each other and couldn't stop laughing! The remainder of the journey consisted of us all belting out Velvet Tones classics, in between fits of laughter. We were so disappointed when we arrived home as we wanted to continue the fun, we will never forget our singing taxi driver!</p>
  <p class="share">Do you have your story? <a href="#">Send</a> us it!</p>
</section>

<footer class="site-footer">
  <p class="copyright">© <span class="name">Ridelark</span> 2011-2012<br><u>Privacy Policy</u></p>
  <span class="social" style="left:736px" aria-label="Social link"></span>
  <span class="social" style="left:768px" aria-label="Social link"></span>
  <span class="social" style="left:801px" aria-label="Social link"></span>
</footer>

</body>
</html>
```